Vital Spark Electrical in need of a business card design

We need a new business card designed for our electrical business. We have a logo already which I will attach below.
Would like the business card to be..
-BLACK background preferably, possibly white back ground behind logo if colours clash.
-White & Blue (logo blue) text
Something that makes the logo pop, & a modern look. Possibly minimal clean format.

REQUIRE:
-Logo on front & back

TEXT TO INCLUDE (ON ONE SIDE):

Tom Harlow
Director/Electrician
M: 0417 365 208
E:info@vitalsparkelectrical-example.com.au
W:www.vitalsparkelectrical-example.com.au
R.E.C 57318

Custom/New Homes
Renovations
Commercial Office/Shop Fit-outs
Communications & Security Cameras
Electric Vehicle Chargers
Airconditioning
Updates

Requirements
Nice to have
• Possibly even lighten the grey shades for the words 'Vital' & 'Spark' to be more easily read on a black background.

```html
<!DOCTYPE html>
<html lang="en">
<head>
<meta charset="utf-8">
<title>Vital Spark Electrical – Business Card</title>
<link rel="stylesheet" href="https://fonts.googleapis.com/css2?family=Montserrat:wght@400;500;700&display=swap">
<style>
  :root {
    --backdrop: #8d8d8f;
    --card: #262626;
    --blue: #139fe0;
    --white: #ffffff;
    --rule: #6a6a6a;
    --soft: #d9d9d9;
  }
  * { margin: 0; padding: 0; box-sizing: border-box; }
  html, body { width: 1200px; height: 800px; overflow: hidden; }
  body {
    background: var(--backdrop);
    font-family: "Montserrat", Arial, sans-serif;
    display: flex;
    align-items: center;
    justify-content: center;
    gap: 40px;
  }
  .card {
    position: relative;
    width: 530px;
    height: 303px;
    background: var(--card);
    border-radius: 18px;
    overflow: hidden;
    color: var(--white);
  }

  /* Contact side */
  .card-contact .edge-band {
    position: absolute; left: 0; right: 0; bottom: 0; height: 7px;
    display: flex;
  }
  .edge-band .blue { flex: 0 0 58%; background: var(--blue); }
  .edge-band .white { flex: 1; background: var(--white); }
  .identity {
    position: absolute; top: 38px; right: 40px;
    display: flex; align-items: center; gap: 16px;
  }
  .identity .brand-mark {
    font-weight: 700; font-size: 13px; color: var(--white);
    display: flex; align-items: center; gap: 7px; letter-spacing: .02em;
  }
  .brand-mark .dot { width: 9px; height: 9px; background: var(--blue); }
  .identity .divider { width: 1px; height: 44px; background: var(--rule); }
  .person-name {
    font-weight: 700; font-size: 23px; color: var(--blue);
    letter-spacing: .04em; text-transform: uppercase; line-height: 1;
  }
  .person-role { font-size: 13px; margin-top: 5px; }
  .contact-list {
    position: absolute; left: 34px; bottom: 38px;
    list-style: none; font-size: 11.5px; line-height: 1.7;
  }
  .contact-list .licence { margin-bottom: 4px; }
  .contact-list li { display: flex; align-items: center; gap: 9px; }
  .contact-list svg { width: 11px; height: 11px; flex: none; }

  /* Services side */
  .card-services .brand-block {
    position: absolute; top: 78px; left: 0; right: 0;
    display: flex; justify-content: center; align-items: center; gap: 12px;
  }
  .card-services .brand-name {
    font-weight: 700; font-size: 34px; color: var(--soft); letter-spacing: .01em;
  }
  .card-services .brand-name .accent { color: var(--blue); }
  .brand-block .dot { width: 16px; height: 16px; background: var(--blue); }
  .services {
    position: absolute; left: 0; right: 0; bottom: 54px;
    text-align: center; font-size: 12px; line-height: 1.75; font-weight: 500;
  }
  .services .sep {
    display: inline-block; width: 5px; height: 5px; background: var(--blue);
    margin: 0 6px 2px;
  }
</style>
</head>
<body>
  <section class="card card-contact">
    <div class="identity">
      <div class="brand-mark"><span class="dot"></span>Vital Spark Electrical</div>
      <span class="divider"></span>
      <div>
        <div class="person-name">Tom Harlow</div>
        <div class="person-role">Director/Electrician</div>
      </div>
    </div>
    <ul class="contact-list">
      <li class="licence">R.E.C 57318</li>
      <li>
        <svg viewBox="0 0 12 12"><rect x="2.5" y="0.8" width="7" height="10.4" rx="1.2" fill="none" stroke="#fff" stroke-width="1.2"/></svg>
        0417 365 208
      </li>
      <li>
        <svg viewBox="0 0 12 12"><rect x="0.5" y="2" width="11" height="8" fill="var(--blue)"/><path d="M0.5 2 6 6.5 11.5 2" fill="none" stroke="#262626" stroke-width="1"/></svg>
        info@vitalsparkelectrical-example.com.au
      </li>
      <li>
        <svg viewBox="0 0 12 12"><circle cx="6" cy="6" r="5.5" fill="var(--blue)"/><path d="M0.5 6h11M6 0.5c-2.5 3-2.5 8 0 11M6 0.5c2.5 3 2.5 8 0 11" fill="none" stroke="#262626" stroke-width=".8"/></svg>
        www.vitalsparkelectrical-example.com.au
      </li>
    </ul>
    <div class="edge-band"><span class="blue"></span><span class="white"></span></div>
  </section>

  <section class="card card-services">
    <div class="brand-block">
      <span class="dot"></span>
      <span class="brand-name">Vital Spark Electrical</span>
    </div>
    <p class="services">
      Custom/New Homes<span class="sep"></span>Renovations<span class="sep"></span>Commercial Office/Shop Fit-outs<br>
      Communications &amp; Security Cameras<span class="sep"></span>Electric Vehicle Chargers<span class="sep"></span>Airconditioning
    </p>
  </section>
</body>
</html>
```